Web landing page design

- Create a Web Design (Uncoded - PSD layout only)

We need a single web page design to promote our service. This page will
acts as a landing page for users and also be utilized in social media
advertising. Please provide us with a cutting edge design. I have attached
a link for what the company is about. In essence we are a photo checking
service which reviews photos for retailers, hotels abd car dealerships to
check everything is good after a service has been performed. Whether it be
a new promotion, cleaning or just checking prices. I am looking for a
design to say that we do many photos and at a very cost effective price
(team based in Mexico)

Link: https://slidora.example/view/kq3Fz8wPnT2dXr7HsLmV/
*Deadline*
5 days
*Updates*

- The Start Here box needs to look like this:

-Start Here (heading)
-A box for email addresses to be entered
-Then a check box with "Yes, I have read and agree to the Privacy Policy
and agree to receive email marketing from Tallumo38'
-A submit button

All of this information needs to be in one box please. And please feel
free to contact me if you have any questions about this.

*Target Market(s)*
Retail business, Merchandising companies, Rental property owners, Car
dealers
Updates

Please can you submit entries. I am just looking for a tidy to a presentation already created. Just needs design touches.

Target Market(s)

Ability for audience to understand concept quickly
Benefits to why to use the product stand out
Technology driven approach

Industry/Entity Type

Retail

Number of Pages Required

1 page

Colors
0792cd

Requirements
Must have
• Clean and modern design

```html
<!DOCTYPE html>
<html lang="en">
<head>
<meta charset="utf-8">
<title>Checkora – Start Here</title>
<link rel="stylesheet" href="https://fonts.googleapis.com/css2?family=Poppins:wght@500;600&family=Arimo:wght@400;700&display=swap">
<style>
  :root {
    --brand: #0792cd;
    --brand-light: #16b0e6;
    --white: #ffffff;
    --placeholder: #8a8a8a;
    --scene-dark: #1c1410;
    --scene-mid: #4a3326;
    --scene-warm: #b97a4a;
    --scene-glow: #f2c68f;
  }
  * { box-sizing: border-box; margin: 0; padding: 0; }
  html, body {
    width: 1200px;
    height: 665px;
    overflow: hidden;
    background: var(--scene-dark);
  }
  .landing {
    position: relative;
    width: 1200px;
    height: 665px;
    overflow: hidden;
    font-family: "Arimo", Arial, sans-serif;
    color: var(--white);
  }
  .hero-photo {
    position: absolute;
    inset: 0;
    background:
      radial-gradient(ellipse 380px 260px at 230px 10px, var(--scene-glow) 0%, rgba(242,198,143,0) 70%),
      radial-gradient(ellipse 330px 380px at 640px 330px, rgba(120,85,65,0.85) 0%, rgba(120,85,65,0) 75%),
      radial-gradient(ellipse 260px 160px at 770px 120px, rgba(150,95,55,0.7) 0%, rgba(150,95,55,0) 80%),
      linear-gradient(180deg, var(--scene-warm) 0%, var(--scene-mid) 38%, var(--scene-dark) 100%);
  }
  .hero-photo::after {
    content: "";
    position: absolute;
    inset: 0;
    background: linear-gradient(180deg, rgba(0,0,0,0) 55%, rgba(0,0,0,0.55) 100%);
  }
  .brand {
    position: absolute;
    left: 0;
    right: 0;
    top: 60px;
    text-align: center;
  }
  .brand-dot {
    display: block;
    width: 58px;
    height: 58px;
    margin: 0 auto;
    border-radius: 50%;
    background: var(--brand);
    transform: translateX(10px);
  }
  .brand-name {
    display: block;
    margin-top: 6px;
    font-family: "Poppins", Arial, sans-serif;
    font-weight: 600;
    font-size: 50px;
    line-height: 1.1;
    letter-spacing: 0.5px;
    color: var(--white);
  }
  .signup {
    position: absolute;
    left: 457px;
    top: 290px;
    width: 286px;
  }
  .signup-title {
    font-family: "Poppins", Arial, sans-serif;
    font-weight: 600;
    font-size: 37px;
    line-height: 52px;
    text-align: center;
    letter-spacing: 0.5px;
    transform: translateX(-6px);
  }
  .email-field {
    display: block;
    width: 286px;
    height: 41px;
    margin-top: 24px;
    padding: 0 24px;
    border: none;
    border-radius: 21px;
    background: var(--white);
    font-family: "Arimo", Arial, sans-serif;
    font-size: 11.5px;
    color: #333;
    outline: none;
  }
  .email-field::placeholder { color: var(--placeholder); }
  .consent {
    display: flex;
    align-items: flex-start;
    gap: 8px;
    margin-top: 19px;
    font-size: 11.6px;
    line-height: 15.5px;
  }
  .consent-box {
    flex: none;
    width: 15px;
    height: 15px;
    margin-top: 1px;
    border-radius: 2px;
    background: var(--white);
    appearance: none;
    -webkit-appearance: none;
    border: none;
  }
  .submit-button {
    display: block;
    width: 148px;
    height: 41px;
    margin: 26px 0 0 69px;
    border: none;
    border-radius: 21px;
    background: linear-gradient(180deg, var(--brand-light) 0%, var(--brand) 100%);
    box-shadow: 0 2px 4px rgba(0,0,0,0.35);
    font-family: "Arimo", Arial, sans-serif;
    font-weight: 700;
    font-size: 13px;
    color: var(--white);
    letter-spacing: 0.2px;
  }
</style>
</head>
<body>
  <main class="landing">
    <div class="hero-photo" role="img" aria-label="Photo of a smiling woman with curly hair looking at her smartphone on a sunlit city street at dusk"></div>

    <header class="brand">
      <span class="brand-dot"></span>
      <span class="brand-name">Checkora</span>
    </header>

    <form class="signup">
      <h1 class="signup-title">Start Here</h1>
      <input class="email-field" type="email" placeholder="Enter Email Address" aria-label="Email address">
      <label class="consent">
        <input class="consent-box" type="checkbox">
        <span>Yes, I have read and agree to the Privacy Policy and<br>&nbsp;agree to receive email marketing from Tallumo38</span>
      </label>
      <button class="submit-button" type="button">SUBMIT</button>
    </form>
  </main>
</body>
</html>
```